Distinctive Men collection for beard oil, beard balm and hand cream

I have a project: a collection for MEN.
The name of my company is KAVRO.
- You can play with the writing of the name without any problem.
- I need a label template for my BEARD oil bottles (it needs to have a place where I can change the skin type: dry skin / normal skin / or oily skin)
- I need a round label template for the 50 ml beard balm for the top of the aluminium can. I would like to use something similar for the hand cream so it would fit.

Example of Ingredients:
Beard oil | Oily skin: Ingrédients : Simmondsia chinensis (Jojoba) Seed Oil *, Corylus avellana (Hazelnut) Oil*, Vitis vinifera Seed Oil*, Trocopherol, parfum.

It is a collection, it needs to fit together!

Thank you :-D

Target Market(s)

MEN with a beard

Colors

Designer to choose colors to be used in the design.

Requirements
Must have
• - Labels for the bottles: 1 3/4' X 4'
• - Round label for the beard balm and the hand cream for men: round 1 3/4'
• - For the bottles: the ingredients goes on one end on the label and the Expiration on the other end, so they are "behind" the bottle. Hope I'm clear, I'm not a desgner ;-)
Nice to have
• I have been looking at labels type, and I like the effect of transparent label on amber buttle, BUT it is not at all a must. Just an observation. I am really open to everything!
Should not have
• Important fact: I don't want black and white like almost every bottles on Zelvane and in barbershop. I want them both to appeal to trendy barbers AND I want them on Zelvane.

```html
<!DOCTYPE html>
<html lang="en">
<head>
<meta charset="utf-8">
<title>KAVRO Hand Cream – Round Lid Label</title>
<link rel="stylesheet" href="https://fonts.googleapis.com/css2?family=Tinos:wght@700&display=swap">
<style>
  :root {
    --page-bg: #efefea;
    --label-taupe: #a5948d;
    --label-teal: #1b4a51;
    --accent-cyan: #4fd2e2;
    --ink-teal: #1b4a51;
  }
  html, body {
    margin: 0;
    padding: 0;
    width: 1200px;
    height: 1160px;
    overflow: hidden;
    background: var(--page-bg);
  }
  .lid-label {
    display: block;
    width: 1200px;
    height: 1160px;
  }
  .label-text {
    font-family: "Tinos", "Times New Roman", serif;
    font-weight: 700;
  }
  .product-word-left { fill: var(--ink-teal); font-size: 100px; }
  .product-word-right { fill: var(--accent-cyan); font-size: 100px; }
  .by-line { fill: var(--accent-cyan); font-size: 34px; }
  .brand-name { fill: var(--accent-cyan); font-size: 110px; }
  .skin-type-box { fill: var(--accent-cyan); }
  .skin-type-text { fill: var(--ink-teal); font-size: 42px; }
  .volume { fill: var(--accent-cyan); font-size: 38px; }
  .half-taupe { fill: var(--label-taupe); }
  .half-teal { fill: var(--label-teal); }
  .inner-ring { fill: none; stroke: var(--accent-cyan); stroke-width: 5; }
</style>
</head>
<body>
<svg class="lid-label" viewBox="0 0 1200 1160" xmlns="http://www.w3.org/2000/svg" role="img" aria-label="KAVRO hand cream round lid label, 50 ml, normal skin">
  <defs>
    <clipPath id="label-disc">
      <circle cx="600" cy="580" r="500"/>
    </clipPath>
    <clipPath id="left-half">
      <rect x="0" y="0" width="664" height="1160"/>
    </clipPath>
  </defs>

  <g class="label-background" clip-path="url(#label-disc)">
    <rect class="half-taupe" x="100" y="80" width="564" height="1000"/>
    <rect class="half-teal" x="664" y="80" width="436" height="1000"/>
  </g>

  <circle class="inner-ring" cx="600" cy="580" r="456" clip-path="url(#left-half)"/>

  <text class="label-text product-word-left" x="650" y="404" text-anchor="end">HAND</text>
  <text class="label-text product-word-right" x="678" y="404">CREAM</text>
  <text class="label-text by-line" x="684" y="480">BY</text>
  <text class="label-text brand-name" x="680" y="600">KAVRO</text>

  <rect class="skin-type-box" x="684" y="712" width="270" height="72"/>
  <text class="label-text skin-type-text" x="819" y="762" text-anchor="middle">Normal skin</text>

  <text class="label-text volume" x="690" y="900">50 ml</text>
</svg>
</body>
</html>
```